Infographic for Commercial Painting and Flooring Company

We need an Infographic that shows a compelling argument for signing on with Verimbos for a maintenance contract vs a project. The infographic should be easily understood visually so sell the story we have provided. 1) What does the quick view give me? 2) Am I interested in this? 3) Does this bring me any value? 4) Is this “everything I have seen before or something new and different”? Included here is a word document called Maintenance vs Project Notes with the written content and instructions, a logo, and two other marketing pieces they currently use so you can see how their brand is being used. Colors should be on brand. I'd like to get this done ASAP if possible. We do not want this piece to look busy.

I added two images called Sample 1 and Sample 2 to portray the types of infographics we like. Simple and clear. Love the watch with the pie chart built in....a smaller version of that would be great for us based on the notes document I provided.

Target Market(s)

Facilities Manufacturers and owners of manufacturing facilities

Font styles to use
Sans Serif

Colors

Designer to choose colors to be used in the design.

Requirements
Must have
• Simple, clean, tell a clear story
Nice to have
• Iconography, pie chart, Men in hard hat
Should not have
• Too many colors. Stick with the brand colors and maybe a few others. Don't want it too look to busy.

```html
<!DOCTYPE html>
<html lang="en">
<head>
<meta charset="utf-8">
<title>Maintenance vs Project – Verimbos</title>
<link rel="stylesheet" href="https://fonts.googleapis.com/css2?family=Montserrat:wght@400;600;700;800&display=swap">
<style>
  :root{
    --navy:#1c3557;
    --blue:#2c6aa8;
    --sky:#dcebf7;
    --green:#6bab3a;
    --olive:#8a9a2c;
    --ink:#1e2a38;
    --grey:#5b6673;
    --white:#ffffff;
    --warm:#f3b23a;
  }
  *{box-sizing:border-box;margin:0;padding:0}
  html,body{width:1200px;height:3000px;overflow:hidden;background:var(--white)}
  body{font-family:"Montserrat",Arial,sans-serif;color:var(--ink)}
  .canvas{position:relative;width:1200px;height:3000px;overflow:hidden;background:var(--white)}

  .title-bar{position:absolute;left:0;top:0;width:1200px;height:130px;background:var(--navy);
    display:flex;align-items:center;justify-content:center}
  .title-bar h1{color:var(--white);font-size:62px;font-weight:800;letter-spacing:2px}

  .intro{position:absolute;left:0;top:160px;width:1200px;height:680px}
  .intro-figure{position:absolute;left:50px;top:40px;width:340px;height:290px;border-radius:14px;
    background:linear-gradient(160deg,#e7eef6,#bcd0e4)}
  .intro-copy{position:absolute;left:50px;top:360px;width:360px}
  .intro-copy h2{font-size:29px;line-height:1.25;font-weight:800;color:var(--navy)}
  .intro-copy p{margin-top:20px;font-size:19px;line-height:1.45;color:var(--grey);font-weight:600}
  .time-pie{position:absolute;left:420px;top:0}
  .pie-label{font-size:17px;font-weight:700;fill:var(--navy)}
  .pie-hours{font-size:34px;font-weight:800;fill:var(--white)}
  .pie-unit{font-size:12px;font-weight:600;fill:var(--white)}

  .cost-band{position:absolute;left:0;top:870px;width:1200px;height:410px;background:var(--sky)}
  .cost-figure{position:absolute;left:50px;top:40px;width:420px;height:330px;border-radius:14px;
    background:linear-gradient(180deg,#9fc0de,#5a88b5)}
  .cost-copy{position:absolute;left:510px;top:45px;width:640px}
  .cost-copy h2{font-size:31px;line-height:1.3;font-weight:800;color:var(--navy);text-align:center}
  .cost-boxes{display:flex;gap:24px;margin-top:36px}
  .cost-box{flex:1;background:var(--navy);color:var(--white);border-radius:10px;padding:26px 22px;
    font-size:21px;line-height:1.4;font-weight:700;text-align:center}

  .solution-arrow{position:absolute;left:0;top:1280px}
  .solution{position:absolute;left:0;top:1390px;width:1200px;text-align:center}
  .solution h2{font-size:66px;font-weight:800;color:var(--green);line-height:1.1}
  .solution h3{font-size:58px;font-weight:800;color:var(--navy);line-height:1.15;margin-top:8px}

  .more-time{position:absolute;left:0;top:1620px;width:1200px}
  .more-time h2{margin-left:70px;font-size:40px;font-weight:800;color:var(--green)}
  .benefits{display:flex;justify-content:space-around;margin-top:46px;padding:0 40px}
  .benefit{width:320px;text-align:center}
  .benefit svg{display:block;margin:0 auto 22px}
  .benefit p{font-size:20px;line-height:1.4;font-weight:600;color:var(--ink)}
  .benefit strong{color:var(--navy)}

  .partner{position:absolute;left:0;top:2040px;width:1200px;height:500px}
  .partner-figure{position:absolute;left:40px;top:20px;width:540px;height:400px;border-radius:50% 50% 14px 14px;
    background:radial-gradient(ellipse at 50% 80%,#2d5f92,#16304f)}
  .partner-copy{position:absolute;left:620px;top:10px;width:560px}
  .partner-copy h2{font-size:30px;line-height:1.25;font-weight:800;color:var(--navy)}
  .partner-list{list-style:none;margin-top:20px}
  .partner-list li{position:relative;padding-left:26px;font-size:19px;line-height:1.38;font-weight:600;color:var(--ink)}
  .partner-list li::before{content:"";position:absolute;left:2px;top:9px;width:10px;height:10px;border-radius:50%;background:var(--green)}
  .aligned{position:absolute;left:600px;top:440px}
  .aligned text{font-size:26px;font-weight:800;fill:var(--white)}

  .pillars{position:absolute;left:150px;top:2570px;width:900px}
  .pillar{display:flex;align-items:center;height:96px}
  .pillar svg{flex:none;margin-right:36px}
  .pillar span{font-size:62px;font-weight:700;color:var(--blue);letter-spacing:1px}

  .brand{position:absolute;left:0;top:2885px;width:1200px;display:flex;align-items:center;justify-content:center;gap:18px}
  .brand-square{width:44px;height:44px;background:var(--navy)}
  .brand-name{font-size:50px;font-weight:800;color:var(--navy)}
</style>
</head>
<body>
<main class="canvas">

  <header class="title-bar"><h1>MAINTENANCE VS PROJECT</h1></header>

  <section class="intro">
    <div class="intro-figure" role="img" aria-label="Illustration of a worker in a yellow hard hat at a laptop, thinking about time"></div>
    <div class="intro-copy">
      <h2>Imagine What You Could Do with An Extra 30% More Time Each Year?</h2>
      <p>Time that you wouldn't need to spend on-boarding a new company every time you have a project or facility upgrade.</p>
    </div>

    <svg class="time-pie" width="780" height="680" viewBox="0 0 780 680" role="img" aria-label="Pie chart of hours spent sourcing and onboarding a vendor">
      <circle cx="400" cy="330" r="200" fill="none" stroke="var(--blue)" stroke-width="10"/>
      <circle cx="400" cy="330" r="185" fill="var(--navy)"/>
      <g transform="translate(400 330)" stroke="var(--white)" stroke-width="5">
        <line x2="0" y2="-185" transform="rotate(0)"/>
        <line x2="0" y2="-185" transform="rotate(48)"/>
        <line x2="0" y2="-185" transform="rotate(132)"/>
        <line x2="0" y2="-185" transform="rotate(180)"/>
        <line x2="0" y2="-185" transform="rotate(204)"/>
        <line x2="0" y2="-185" transform="rotate(240)"/>
        <line x2="0" y2="-185" transform="rotate(276)"/>
        <line x2="0" y2="-185" transform="rotate(312)"/>
      </g>
      <circle cx="400" cy="330" r="30" fill="var(--white)"/>
      <g text-anchor="middle">
        <text class="pie-hours" x="453" y="223">4</text><text class="pie-unit" x="453" y="240">hrs</text>
        <text class="pie-hours" x="525" y="338">7</text><text class="pie-unit" x="525" y="355">hrs</text>
        <text class="pie-hours" x="453" y="447">4</text><text class="pie-unit" x="453" y="464">hrs</text>
        <text class="pie-hours" x="374" y="463">2</text><text class="pie-unit" x="374" y="480">hrs</text>
        <text class="pie-hours" x="316" y="428">3</text><text class="pie-unit" x="316" y="445">hrs</text>
        <text class="pie-hours" x="278" y="368">3</text><text class="pie-unit" x="278" y="385">hrs</text>
        <text class="pie-hours" x="286" y="285">3</text><text class="pie-unit" x="286" y="302">hrs</text>
        <text class="pie-hours" x="347" y="222">4</text><text class="pie-unit" x="347" y="239">hrs</text>
      </g>
      <text class="pie-label" x="505" y="70"><tspan x="505">1. Source</tspan><tspan x="505" dy="21">Vendors &amp;</tspan><tspan x="505" dy="21">Bidders</tspan></text>
      <text class="pie-label" x="618" y="300"><tspan x="618">2. Schedule and</tspan><tspan x="618" dy="21">Completing a</tspan><tspan x="618" dy="21">Walkthrough</tspan></text>
      <text class="pie-label" x="515" y="560"><tspan x="515">3. Reviewing</tspan><tspan x="515" dy="21">Estimates</tspan></text>
      <text class="pie-label" text-anchor="middle" x="355" y="575"><tspan x="355">4. Phone calls to clarify</tspan><tspan x="355" dy="21">scope and any big</tspan><tspan x="355" dy="21">revisions</tspan></text>
      <text class="pie-label" text-anchor="end" x="235" y="480"><tspan x="235">5. Present to</tspan><tspan x="235" dy="21">Decision Maker &amp;</tspan><tspan x="235" dy="21">Financing Approval</tspan></text>
      <text class="pie-label" text-anchor="end" x="170" y="330"><tspan x="170">6. Negotiations</tspan><tspan x="170" dy="21">with Vendor</tspan></text>
      <text class="pie-label" text-anchor="end" x="190" y="190"><tspan x="190">7. Awarding &amp;</tspan><tspan x="190" dy="21">Purchasing</tspan></text>
      <text class="pie-label" text-anchor="middle" x="290" y="40"><tspan x="290">8. Completing</tspan><tspan x="290" dy="21">On-Boarding</tspan><tspan x="290" dy="21">Paperwork</tspan></text>
    </svg>
  </section>

  <section class="cost-band">
    <div class="cost-figure" role="img" aria-label="Illustration of hands typing on a laptop keyboard"></div>
    <div class="cost-copy">
      <h2>It Takes 30+ Hours to Source and Onboard the Most Qualified Vendor…YIKES!</h2>
      <div class="cost-boxes">
        <div class="cost-box">20 Projects = 600 Hours or 25% of Your Time Per Year… UGH!</div>
        <div class="cost-box">On-Boarding Once = 1.5% of Your Time for the entire year…FOR REAL!</div>
      </div>
    </div>
  </section>

  <svg class="solution-arrow" width="1200" height="120" viewBox="0 0 1200 120" aria-hidden="true">
    <path d="M1100 10 V50 H90 V95" fill="none" stroke="var(--olive)" stroke-width="10" stroke-linejoin="round"/>
    <polygon points="70,92 110,92 90,118" fill="var(--olive)"/>
  </svg>

  <section class="solution">
    <h2>A Better Solution:</h2>
    <h3>A Preventative Maintenance Program</h3>
  </section>

  <section class="more-time">
    <h2>You'll Have More Time to…</h2>
    <div class="benefits">
      <div class="benefit">
        <svg width="120" height="140" viewBox="0 0 120 140" aria-hidden="true">
          <rect x="30" y="8" width="60" height="124" rx="10" fill="var(--navy)"/>
          <rect x="37" y="22" width="46" height="88" fill="var(--sky)"/>
          <rect x="42" y="34" width="36" height="10" rx="3" fill="var(--green)"/>
          <rect x="42" y="52" width="30" height="10" rx="3" fill="var(--blue)"/>
          <rect x="42" y="70" width="36" height="10" rx="3" fill="var(--green)"/>
          <circle cx="60" cy="121" r="5" fill="var(--white)"/>
        </svg>
        <p><strong>Focus on Communication</strong> with Your Team and Customers</p>
      </div>
      <div class="benefit">
        <svg width="120" height="140" viewBox="0 0 120 140" aria-hidden="true">
          <polygon points="60,8 96,124 24,124" fill="var(--warm)"/>
          <polygon points="48,48 72,48 78,68 42,68" fill="var(--white)"/>
          <polygon points="36,88 84,88 89,104 31,104" fill="var(--white)"/>
          <rect x="12" y="122" width="96" height="12" rx="3" fill="var(--navy)"/>
        </svg>
        <p><strong>Focus on Safety</strong> to ensure it is a priority</p>
      </div>
      <div class="benefit">
        <svg width="140" height="140" viewBox="0 0 140 140" aria-hidden="true">
          <g transform="translate(58 78)">
            <circle r="38" fill="var(--blue)"/>
            <g fill="var(--blue)">
              <rect x="-8" y="-50" width="16" height="16"/><rect x="-8" y="34" width="16" height="16"/>
              <rect x="-50" y="-8" width="16" height="16"/><rect x="34" y="-8" width="16" height="16"/>
            </g>
            <circle r="14" fill="var(--white)"/>
          </g>
          <g transform="translate(108 36)">
            <circle r="22" fill="var(--green)"/>
            <g fill="var(--green)">
              <rect x="-6" y="-30" width="12" height="10"/><rect x="-6" y="20" width="12" height="10"/>
              <rect x="-30" y="-6" width="10" height="12"/><rect x="20" y="-6" width="10" height="12"/>
            </g>
            <circle r="8" fill="var(--white)"/>
          </g>
        </svg>
        <p><strong>Focus on Productivity</strong> to ensure you meet all of your business unit's needs</p>
      </div>
    </div>
  </section>

  <section class="partner">
    <div class="partner-figure" role="img" aria-label="Illustration of two businessmen shaking hands on a circular platform"></div>
    <div class="partner-copy">
      <h2>You'll Have A Trusted Partner Who Provides…</h2>
      <ul class="partner-list">
        <li>Safety is Our #1 Objective</li>
        <li>Adapting to all of Your Scheduling Requirements</li>
        <li>A Single Point of Communication</li>
        <li>Integration w/ your Work Order Process &amp; Project Tracking</li>
        <li>A Dedicated Field Team, who Understands the Ins and Outs of Your Facility</li>
        <li>Rapid Response Time</li>
        <li>All Tasks and Jobs (Big or Small) Equally Prioritized</li>
        <li>Customized Billing and Future Budget Building</li>
        <li>Visual Facility Mapping</li>
      </ul>
    </div>
    <svg class="aligned" width="580" height="64" viewBox="0 0 580 64" aria-hidden="true">
      <polygon points="0,6 520,6 520,0 580,32 520,64 520,58 0,58" fill="var(--olive)"/>
      <text x="40" y="41">Aligned with Your Needs</text>
    </svg>
  </section>

  <section class="pillars">
    <div class="pillar">
      <svg width="80" height="80" viewBox="0 0 80 80" aria-hidden="true">
        <path d="M16 34 A25 25 0 0 1 62 26" fill="none" stroke="var(--blue)" stroke-width="8"/>
        <polygon points="54,14 72,26 54,36" fill="var(--blue)"/>
        <path d="M64 46 A25 25 0 0 1 18 54" fill="none" stroke="var(--green)" stroke-width="8"/>
        <polygon points="26,66 8,54 26,44" fill="var(--green)"/>
      </svg>
      <span>Consistency</span>
    </div>
    <div class="pillar">
      <svg width="80" height="80" viewBox="0 0 80 80" aria-hidden="true">
        <rect x="10" y="50" width="12" height="22" fill="var(--blue)"/>
        <rect x="30" y="38" width="12" height="34" fill="var(--blue)"/>
        <rect x="50" y="24" width="12" height="48" fill="var(--blue)"/>
        <polyline points="8,40 30,24 48,30 70,8" fill="none" stroke="var(--green)" stroke-width="6"/>
      </svg>
      <span>Predictability</span>
    </div>
    <div class="pillar">
      <svg width="80" height="80" viewBox="0 0 80 80" aria-hidden="true">
        <path d="M40 4 L70 16 V38 C70 58 56 70 40 76 C24 70 10 58 10 38 V16 Z" fill="var(--navy)"/>
        <polyline points="26,40 36,50 56,30" fill="none" stroke="var(--green)" stroke-width="8"/>
      </svg>
      <span>Reliability</span>
    </div>
  </section>

  <footer class="brand">
    <div class="brand-square"></div>
    <div class="brand-name">Verimbos</div>
  </footer>

</main>
</body>
</html>
```